Design packaging for our 'Cindral Wisp' personal massager (vibrator)!

Design our product box, please.

We will be selling a vibrator (personal massager on the website:-) ) in 4 different colours - please see attached. The box will be matt black, and we would love classy and understated, definitely not garish or raunchy. Note that the Barcode has to be on a white background, so we suspect we will need to stick that onto the box somewhere - probably the bottom, unless anyone has a better (more aesthetically pleasing) idea! Dimensions of the barcode must be between 1 inch x 2 inches and 2 inches x 3 inches(1 inch x 3 inches, or 2 inches by 2 inches, for eg) - if you can propose a spot, that would be great. The product has a pink satin travel pouch in the box, and product comes in pink, purple, Rose and Black. The box needs to stand out in photography, and the product will be sold online. Could add 'Heated Massager' somewhere, and colour of the product, too. Certifications that would be good to have on the box: CE and ROHS. There is a small insert box for the charger wire - would want 'Charger Wire' in matching script on this box. Script to match product name, please.

We included a potential logo for the box, and also our company logo. We are open to suggestions on the logo for the box, but the product name is Cindral Wisp (spelling intentionally different from Co. name), and it should tie in with our company logo in some way.

We will be super quick in obtaining any additional information required from the supplier, or answering any questions.

Target Market(s)

Audience: Mostly women (of all ages, hopefully)! Realistically, they'll be between the ages of 18 and 40 for the most part. They will be American (that's where our market is, but we anticipate moving to UK, Australia and Europe. Middle to high income earners. We expect they will be looking for subtlety and quality.

Font styles to use
Other font styles liked:
• See Product name logo attachment

Colors

Designer to choose colors to be used in the design.

Requirements
Must have
• Convey quality, understatement and link to our company logo in some way. Should stand out when photographed, and compared to competitors on online forum!
Should not have
• Crass, raunchy feel. No pictures of vibrators.

```html
<!DOCTYPE html>
<html lang="en">
<head>
<meta charset="utf-8">
<title>Cindral Wisp – Heated Massager box dieline</title>
<link rel="stylesheet" href="https://fonts.googleapis.com/css2?family=Oswald:wght@300&family=Raleway:wght@400&family=Roboto:wght@400;700&display=swap">
<style>
  :root {
    --backdrop: #e4e4e4;
    --board: #0b0b0b;
    --lilac: #9b6fc4;
    --pattern-a: #2a1838;
    --pattern-b: #4a2c63;
    --cut-line: #d0141c;
    --ink-light: #f2f2f2;
    --ink-soft: #c8c8c8;
    --swatch-pink: #d6145f;
  }
  html, body {
    margin: 0;
    width: 1200px;
    height: 1200px;
    overflow: hidden;
    background: var(--backdrop);
  }
  .dieline {
    position: absolute;
    left: 286px;
    top: 40px;
    width: 628px;
    height: 1120px;
  }
  .board { fill: var(--board); }
  .cut { fill: none; stroke: var(--cut-line); stroke-width: 1.4; }
  .brand-name { font-family: "Raleway", sans-serif; font-weight: 400; fill: var(--lilac); }
  .brand-maker { font-family: "Roboto", sans-serif; fill: var(--ink-soft); }
  .brand-dot { fill: none; stroke: var(--lilac); stroke-width: 1.6; }
  .headline { font-family: "Oswald", sans-serif; font-weight: 300; fill: var(--ink-light); }
  .seal { fill: var(--board); stroke: var(--ink-light); stroke-width: 1.6; }
  .fine { font-family: "Roboto", sans-serif; fill: var(--ink-light); }
  .fine-bold { font-family: "Roboto", sans-serif; font-weight: 700; fill: var(--ink-light); }
  .spec-box { fill: var(--board); stroke: var(--ink-soft); stroke-width: 0.6; }
  .spec-rule { stroke: var(--ink-soft); stroke-width: 0.4; }
  .text-backing { fill: var(--board); }
  .icon-frame { fill: none; stroke: var(--ink-light); stroke-width: 1.4; }
  .icon-line { fill: none; stroke: var(--ink-light); stroke-width: 1.3; stroke-linecap: round; }
  .cert-mark { fill: none; stroke: var(--ink-light); stroke-width: 1.4; }
  .swatch { fill: var(--swatch-pink); }
</style>
</head>
<body>
<svg class="dieline" viewBox="793 245 589 1050" xmlns="http://www.w3.org/2000/svg">
  <defs>
    <linearGradient id="scale-tone" x1="0" y1="0" x2="0" y2="1">
      <stop offset="0" stop-color="var(--pattern-a)"/>
      <stop offset="1" stop-color="var(--pattern-b)"/>
    </linearGradient>
  </defs>

  <!-- board outline -->
  <g class="board-shape">
    <rect class="board" x="975" y="245" width="224" height="175"/>
    <path class="board" d="M819 373 H960 L972 415 H819 Z"/>
    <path class="board" d="M1356 373 H1215 L1203 415 H1356 Z"/>
    <rect class="board" x="793" y="415" width="589" height="707"/>
    <path class="board" d="M819 1122 H972 L960 1166 H819 Z"/>
    <path class="board" d="M1356 1122 H1203 L1215 1166 H1356 Z"/>
    <rect class="board" x="975" y="1122" width="224" height="173"/>
  </g>

  <!-- scale pattern areas -->
  <rect class="pattern-band" x="793" y="415" width="589" height="54" fill="url(#scale-tone)" role="img" aria-label="Lilac scalloped fish-scale pattern band"/>
  <rect class="pattern-field" x="793" y="828" width="589" height="294" fill="url(#scale-tone)" role="img" aria-label="Lilac scalloped fish-scale pattern field"/>

  <!-- cut and fold lines -->
  <line class="cut" x1="975" y1="300" x2="1199" y2="300"/>
  <rect class="cut" x="858" y="415" width="114" height="707"/>
  <rect class="cut" x="972" y="415" width="231" height="707"/>
  <rect class="cut" x="1203" y="415" width="114" height="707"/>
  <line class="cut" x1="975" y1="1237" x2="1199" y2="1237"/>

  <!-- top tuck panel -->
  <g class="top-brand">
    <circle class="brand-dot" cx="1082" cy="327" r="13"/>
    <text class="brand-name" x="1082" y="374" font-size="15" text-anchor="middle">Cindral Wisp</text>
    <text class="brand-maker" x="1082" y="389" font-size="7" text-anchor="middle">by Halvenne Co</text>
  </g>

  <!-- front panel -->
  <g class="front-brand">
    <circle class="brand-dot" cx="1087" cy="535" r="24"/>
    <text class="brand-name" x="1087" y="612" font-size="28" text-anchor="middle">Cindral Wisp</text>
    <text class="brand-maker" x="1087" y="637" font-size="12" text-anchor="middle">by Halvenne Co</text>
  </g>
  <g class="product-seal">
    <circle class="seal" cx="1087" cy="826" r="88"/>
    <text class="headline" x="1087" y="819" font-size="32" text-anchor="middle">HEATED</text>
    <text class="headline" x="1087" y="856" font-size="32" text-anchor="middle">MASSAGER</text>
  </g>
  <g class="feature-icons">
    <rect class="text-backing" x="992" y="1072" width="36" height="38"/>
    <rect class="icon-frame" x="994" y="1074" width="32" height="34" rx="4"/>
    <rect class="icon-line" x="1003" y="1080" width="5" height="17" rx="2.5"/>
    <circle class="icon-line" cx="1005.5" cy="1100" r="4"/>
    <path class="icon-line" d="M1015 1085 h6 M1018 1082 v6 M1014 1094 h7 M1014 1098 h7 M1014 1102 h7"/>
    <rect class="text-backing" x="1036" y="1072" width="36" height="38"/>
    <rect class="icon-frame" x="1038" y="1074" width="32" height="34" rx="4"/>
    <rect class="icon-line" x="1049" y="1079" width="10" height="12" rx="1"/>
    <path class="icon-line" d="M1052 1083 h1 M1055 1083 h1 M1050 1091 h8 l-2 6 h-4 Z M1054 1097 v6"/>
  </g>
  <g class="certifications">
    <rect class="text-backing" x="1126" y="1084" width="56" height="26" rx="13"/>
    <rect class="cert-mark" x="1130" y="1089" width="18" height="16" rx="2"/>
    <circle class="cert-mark" cx="1167" cy="1097" r="10"/>
  </g>

  <!-- left side panel -->
  <g class="spec-table">
    <rect class="spec-box" x="866" y="937" width="94" height="51"/>
    <text class="fine-bold" x="872" y="945" font-size="6.2">Speed</text>
    <text class="fine-bold" x="914" y="945" font-size="6.2">Temperature</text>
    <line class="spec-rule" x1="866" y1="948" x2="960" y2="948"/>
    <text class="fine" x="872" y="955" font-size="6">Extra Slow</text>
    <text class="fine" x="914" y="955" font-size="6">100°F-120°F</text>
    <line class="spec-rule" x1="866" y1="958" x2="960" y2="958"/>
    <text class="fine" x="872" y="965" font-size="6">Slow</text>
    <text class="fine" x="914" y="965" font-size="6">80°F-100°F</text>
    <line class="spec-rule" x1="866" y1="968" x2="960" y2="968"/>
    <text class="fine" x="872" y="975" font-size="6">Medium</text>
    <text class="fine" x="914" y="975" font-size="6">68°F-80°F</text>
    <line class="spec-rule" x1="866" y1="978" x2="960" y2="978"/>
    <text class="fine" x="872" y="985" font-size="6">Fast</text>
    <text class="fine" x="914" y="985" font-size="6">50°F-68°F</text>
  </g>
  <g class="maker-contact">
    <rect class="text-backing" x="862" y="999" width="106" height="94"/>
    <text class="fine-bold" x="866" y="1011" font-size="8">Halvenne Co</text>
    <text class="fine" x="866" y="1024" font-size="7">42 Larkspur Row,</text>
    <text class="fine" x="866" y="1033" font-size="7">Fenwick, CA 90000</text>
    <text class="fine" x="866" y="1043" font-size="7">(555) 014-2286</text>
    <text class="fine" x="866" y="1052" font-size="7">hello@halvenne.example</text>
    <text class="fine" x="866" y="1062" font-size="7">www.halvenne.example</text>
    <text class="fine-bold" x="866" y="1087" font-size="7">Made in USA</text>
  </g>

  <!-- right side panel -->
  <g class="disclaimer">
    <rect class="text-backing" x="1210" y="932" width="102" height="118"/>
    <text class="fine" font-size="6.3" text-anchor="middle">
      <tspan x="1260" y="943">This product is sold without</tspan>
      <tspan x="1260" y="952">implied warranties beyond</tspan>
      <tspan x="1260" y="961">those stated by law. It is</tspan>
      <tspan x="1260" y="970">made from quality materials.</tspan>
      <tspan x="1260" y="979">The buyer is responsible</tspan>
      <tspan x="1260" y="988">for deciding whether it</tspan>
      <tspan x="1260" y="997">suits the intended use.</tspan>
      <tspan x="1260" y="1006">Seller liability is limited</tspan>
      <tspan x="1260" y="1015">to the purchase price.</tspan>
    </text>
  </g>
  <g class="colour-variant">
    <rect class="text-backing" x="1224" y="1056" width="80" height="38" rx="8"/>
    <circle class="swatch" cx="1245" cy="1075" r="15"/>
    <text class="fine-bold" x="1269" y="1072" font-size="7.5">Pink</text>
    <text class="fine-bold" x="1268" y="1083" font-size="7.5">Color</text>
  </g>

  <!-- bottom panel -->
  <text class="fine" x="1082" y="1225" font-size="7" text-anchor="middle">Made in USA</text>
</svg>
</body>
</html>
```